Landing Page

basically our company has as an strategy to sell our subscription product a set os pages normally in 4 steps
1 - We show that the "customer" will win a prizze
2 - We show some advantages that we have as a company
3 - We show another prizze
4 - We explain that to gain all itens they should make a subscription with a HUGE discount
What do we need?
1 - a new proposal for our set of landing pages
2 - responsive layout for all pages
3 - ideas that can increase our conversion rates
Examples:
http://www.saibatudoagora.com/
http://www.saibatudoagora.com/camfly/index.php
http://www.saibatudoagora.com/pixelcart/index.php
http://www.saibatudoagora.com/v2/index.php
http://servicoglobal.guardiaq.org.br/index.aspx?prm_id_c=PZM13001
http://www.brindelar.com.br/br_rdb_pro_vsi_int_1.asp?mktcode=RDPN50
https://www.linkaro77.info/seq2012/twosteps/pt_br/b2013/index.html?lang=brpt_br&project=TwoSteps&codeprom=ECAD0901&tmpl=b2013&cn=EE00AE90-96EA-4C4D-9AC0-6E9CB5476B41#1
https://servicoglobal.guardiaq.org.br/step_03.aspx
It Company

```html
<!DOCTYPE html>
<html lang="en">
<head>
<meta charset="utf-8">
<title>Guardiaq – Sign Up</title>
<link href="https://fonts.googleapis.com/css2?family=Open+Sans:wght@300;400;600;700&display=swap" rel="stylesheet">
<style>
:root{
  --green-dark:#0c3a24;
  --green-mid:#145a34;
  --green-band:#0f4a2a;
  --lime:#86b800;
  --lime-dark:#5f8a00;
  --page:#ebebeb;
  --panel:#f4f4f4;
  --ink:#333;
  --muted:#555;
  --line:#cfcfcf;
  --white:#fff;
}
*{box-sizing:border-box;margin:0;padding:0}
html,body{width:1200px;height:961px;overflow:hidden}
body{position:relative;background:var(--page);font-family:'Open Sans',Arial,sans-serif;color:var(--ink)}
.hero{position:absolute;left:0;top:0;width:1200px;height:464px;
  background:radial-gradient(ellipse at 55% 45%,#1d6b43 0%,var(--green-mid) 35%,var(--green-dark) 100%)}
.logo{position:absolute;left:172px;top:19px;display:flex;align-items:center;gap:10px}
.logo-mark{width:22px;height:22px;background:var(--lime);border-radius:50%}
.logo-name{font-size:36px;font-weight:700;color:var(--white);letter-spacing:1px}
.social{position:absolute;left:922px;top:50px;display:flex;gap:6px}
.social span{width:30px;height:30px;border-radius:50%;background:var(--white)}
.social span:nth-child(2){background:#9aa99f}
.showcase{position:absolute;left:118px;top:127px;width:592px;height:352px}
.showcase-frame{position:absolute;left:56px;top:0;width:480px;height:320px;background:#111;border-radius:14px 14px 0 0;border:2px solid #999}
.showcase-base{position:absolute;left:0;top:320px;width:592px;height:20px;background:linear-gradient(#e8e8e8,#9a9a9a);border-radius:0 0 50% 50%/0 0 100% 100%}
.showcase-photo{position:absolute;left:16px;top:18px;width:450px;height:281px;background:linear-gradient(135deg,#c88a5a,#8d7c70 45%,#e6e3dd)}
.showcase-caption{position:absolute;left:16px;top:250px;width:450px;height:49px;background:rgba(0,0,0,.55);color:var(--white);font-weight:300;font-size:23px;display:flex;align-items:center;justify-content:center;letter-spacing:.5px}
.signup{position:absolute;left:769px;top:125px;width:294px;height:339px;background:var(--panel);border-radius:3px 3px 0 0;padding:20px 20px 0}
.signup h2{font-weight:400;font-size:28px;color:#222;padding-bottom:6px;border-bottom:1px solid #d6d6d6}
.signup p{font-size:12.5px;line-height:18px;margin:10px 0 12px;color:#333}
.field{display:block;width:255px;height:39px;border:1px solid #c8c8c8;background:var(--white);font-size:12.5px;color:#777;padding:0 13px;line-height:37px;margin-bottom:8px;margin-left:-1px}
.btn-next{display:block;width:255px;height:51px;background:var(--lime);border-bottom:5px solid var(--lime-dark);color:var(--white);font-weight:600;font-size:23px;text-align:center;line-height:46px;margin-top:10px}
.section-title{position:absolute;font-size:17px;font-weight:400;color:#333}
.thumb{position:absolute;width:176px;height:135px}
.thumb-tech{left:118px;top:571px;background:linear-gradient(135deg,#0b3c66,#2aa3d8 55%,#0a2a4a)}
.thumb-gift{left:641px;top:571px;background:linear-gradient(135deg,#f5b9b7,#f2a3a5 50%,#f9d3cf)}
.blurb{position:absolute;width:252px;font-size:11.5px;line-height:17px;color:#444}
.btn-more{position:absolute;width:95px;height:29px;background:var(--lime);border-bottom:2px solid var(--lime-dark);color:var(--white);font-size:13px;text-align:center;line-height:27px}
.divider{position:absolute;left:602px;top:556px;width:1px;height:160px;background:var(--line)}
.offer{position:absolute;left:118px;top:755px;width:965px;height:160px;
  background:radial-gradient(circle at 80% 40%,#1c6b3a,var(--green-band) 60%,#0b3d22)}
.offer h3{position:absolute;left:22px;top:21px;font-weight:400;font-size:25px;color:var(--white)}
.offer p{position:absolute;left:21px;top:62px;font-size:19px;color:var(--white)}
.btn-subscribe{position:absolute;left:21px;top:97px;width:181px;height:44px;background:var(--lime);border-bottom:4px solid var(--lime-dark);color:var(--white);font-weight:600;font-size:16px;text-align:center;line-height:40px}
.deal{position:absolute;left:770px;top:38px;width:147px;color:var(--white);text-align:center}
.deal-now{display:flex;align-items:center;gap:10px;font-size:11px;font-weight:600}
.deal-now::before,.deal-now::after{content:"";flex:1;height:1px;background:var(--white)}
.deal-value{position:relative;font-size:68px;font-weight:400;line-height:1;margin-top:6px;text-align:left;padding-left:20px}
.deal-pct{position:absolute;left:106px;top:2px;font-size:38px}
.deal-off{position:absolute;left:108px;top:44px;font-size:18px}
.footer{position:absolute;left:0;top:926px;width:1200px;text-align:center;font-size:13px;color:#666}
</style>
</head>
<body>
<header class="hero">
  <div class="logo"><span class="logo-mark"></span><span class="logo-name">GUARDIAQ</span></div>
  <nav class="social" aria-label="Social links"><span></span><span></span><span></span><span></span></nav>
  <div class="showcase">
    <div class="showcase-frame">
      <div class="showcase-photo" role="img" aria-label="Photo of a customer receiving a boxed tablet prize from a company representative"></div>
      <div class="showcase-caption">CUSTOMER WIN A PRIZZE</div>
    </div>
    <div class="showcase-base"></div>
  </div>
  <form class="signup">
    <h2>SIGN UP HERE</h2>
    <p>It is a long established fact that a reader will be distracted by the readable</p>
    <span class="field">Your Name</span>
    <span class="field">Your Email</span>
    <span class="field">CPF:</span>
    <span class="btn-next">NEXT STEP</span>
  </form>
</header>

<h2 class="section-title" style="left:118px;top:527px">SOME ADVANTAGES THAT WE HAVE AS A COMPANY</h2>
<div class="thumb thumb-tech" role="img" aria-label="Hands using a smartphone with floating app icons"></div>
<p class="blurb" style="left:314px;top:567px">It is a long established fact that a reader will be distracted by the readable content of a page when looking at its layout. The point of using Lorem Ipsum is that it has a more-or-less normal distribution of letters, as opposed to using 'Content here, content here.</p>
<span class="btn-more" style="left:315px;top:677px">View More</span>

<div class="divider"></div>

<h2 class="section-title" style="left:638px;top:530px;font-size:19px">PRIZZE</h2>
<div class="thumb thumb-gift" role="img" aria-label="Hands exchanging a gift box tied with a red ribbon"></div>
<p class="blurb" style="left:837px;top:567px">It is a long established fact that a reader will be distracted by the readable content of a page when looking at its layout. The point of using Lorem Ipsum is that it has a more-or-less normal distribution of letters, as opposed to using 'Content here, content here.</p>
<span class="btn-more" style="left:838px;top:677px">View More</span>

<section class="offer">
  <h3>Hurry! Limited Time Offer</h3>
  <p>Subscribe Today &amp; Save? Huge sale on our best Selling product</p>
  <span class="btn-subscribe">SUBSCRIBE NOW</span>
  <div class="deal">
    <div class="deal-now">NOW</div>
    <div class="deal-value">50<span class="deal-pct">%</span><span class="deal-off">OFF</span></div>
  </div>
</section>

<footer class="footer">© 2014 Pagelift.com</footer>
</body>
</html>
```